Redesign of WordHarbor.com in Bootstrap 4

Current design of WordHarbor.com is not responsive. We need to change it to latest version of Bootstrap 4 keeping essential elements in place.

Apart from home page, we need designs for http://www.wordharbor.com/meaning/cat also.

Coding

Coded - Design and coding required

Number of Pages Required

2 page

Colors
34a7d8

Requirements
Must have
• Bootstrap 4

```html
<!DOCTYPE html>
<html lang="en">
<head>
<meta charset="utf-8">
<title>Cat – WordHarbor</title>
<link href="https://fonts.googleapis.com/css2?family=Oswald:wght@400&family=Roboto:wght@400;500&display=swap" rel="stylesheet">
<style>
  :root{
    --brand:#34a7d8;
    --header:#26272d;
    --input:#2f3036;
    --ink:#222;
    --muted:#777;
    --card:#f9f9f9;
    --line:#e6e6e6;
    --cell-alt:#dcdcdc;
  }
  *{box-sizing:border-box;margin:0;padding:0}
  html,body{width:1200px;height:1200px;overflow:hidden;background:#fff;font-family:"Roboto",sans-serif;color:var(--ink)}
  .page{position:relative;width:1200px;height:1200px;overflow:hidden}
  .site-header{position:absolute;left:0;top:0;width:1200px;height:105px;background:var(--header)}
  .brand{position:absolute;left:131px;top:0;width:104px;height:105px;background:#fff;display:flex;align-items:center;justify-content:center;flex-direction:column;gap:6px}
  .brand-mark{width:14px;height:14px;background:var(--brand)}
  .brand-name{font-size:14px;font-weight:500;color:var(--brand)}
  .search{position:absolute;left:379px;top:25px;width:367px;height:38px;display:flex}
  .search-input{flex:1;background:var(--input);border:1px solid #3a3b41;color:#999;font-size:13px;padding:0 11px;display:flex;align-items:center}
  .search-btn{width:42px;background:var(--brand);display:flex;align-items:center;justify-content:center}
  .search-hint{position:absolute;left:390px;top:71px;font-size:9px;color:#9a9a9a}
  .account{position:absolute;left:925px;top:22px;font-size:10.5px;color:var(--brand);font-weight:500}
  .menu-toggle{position:absolute;left:1047px;top:16px}
  .page-title{position:absolute;left:0;top:150px;width:1200px;text-align:center;font-family:"Oswald",sans-serif;font-weight:400;font-size:56px;line-height:1;color:var(--brand)}
  .title-rule{position:absolute;left:581px;top:222px;width:32px;height:3px;background:var(--brand)}
  .browse{position:absolute;left:0;top:250px;width:1200px;height:136px;background:var(--brand)}
  .browse h2{position:absolute;left:0;top:24px;width:1200px;text-align:center;font-family:"Oswald",sans-serif;font-weight:400;font-size:34px;line-height:1;color:#fff}
  .alphabet{position:absolute;left:225px;top:86px;display:flex}
  .alphabet span{width:28.8px;height:29px;display:flex;align-items:center;justify-content:center;font-size:19px;color:#666;background:#fff}
  .alphabet span:nth-child(even){background:var(--cell-alt)}
  .entry{position:absolute;left:131px;width:937px;background:var(--card);border:1px solid var(--line);overflow:hidden}
  .entry-head{padding:15px 12px 0}
  .entry-word{display:flex;align-items:center;gap:8px;font-size:16px;color:var(--brand)}
  .entry-summary{margin-top:9px;font-size:12.7px;font-weight:500}
  .entry-body{position:absolute;left:0;top:76px;width:935px;height:520px;background:#fff;border-top:1px solid var(--line);padding:0 11px}
  .section{border-bottom:1px solid var(--line);padding:10px 1px 12px}
  .section:last-child{border-bottom:0}
  .section h3{font-size:13px;font-weight:400;color:var(--muted)}
  .section h3 b{font-weight:400;color:var(--ink)}
  .section ul{list-style:none;margin-top:13px}
  .section li{font-size:12.8px;line-height:20.8px;color:#333}
  .more{display:block;margin-top:3px;font-size:10.5px;color:var(--brand)}
  .synonyms{margin-top:13px;font-size:12.8px;color:var(--brand)}
  .actions{display:flex;gap:16px;margin-top:20px}
  .btn{height:34px;background:var(--brand);color:#fff;font-size:12.6px;display:flex;align-items:center;padding:0 19px}
</style>
</head>
<body>
<div class="page">
<header class="site-header">
  <div class="brand"><span class="brand-mark"></span><span class="brand-name">WordHarbor</span></div>
  <div class="search">
    <div class="search-input">Cat</div>
    <div class="search-btn">
      <svg width="22" height="22" viewBox="0 0 22 22"><circle cx="9" cy="9" r="6.5" fill="none" stroke="#fff" stroke-width="2.2"/><line x1="13.8" y1="13.8" x2="20" y2="20" stroke="#fff" stroke-width="2.6" stroke-linecap="round"/></svg>
    </div>
  </div>
  <div class="search-hint">(eg. tone, summary, music)</div>
  <div class="account">Login | Register</div>
  <svg class="menu-toggle" width="22" height="16" viewBox="0 0 22 16"><rect y="0" width="22" height="2.4" fill="#fff"/><rect y="6.5" width="22" height="2.4" fill="#fff"/><rect y="13" width="22" height="2.4" fill="#fff"/></svg>
</header>

<h1 class="page-title">Cat</h1>
<div class="title-rule"></div>

<section class="browse">
  <h2>Browse Dictionary</h2>
  <nav class="alphabet">
    <span>A</span><span>B</span><span>C</span><span>D</span><span>E</span><span>F</span><span>G</span><span>H</span><span>I</span><span>J</span><span>K</span><span>L</span><span>M</span><span>N</span><span>O</span><span>P</span><span>Q</span><span>R</span><span>S</span><span>T</span><span>U</span><span>V</span><span>W</span><span>X</span><span>Y</span><span>Z</span>
  </nav>
</section>

<article class="entry" style="top:406px;height:598px">
  <div class="entry-head">
    <div class="entry-word">Cat <svg width="17" height="17" viewBox="0 0 17 17"><circle cx="8.5" cy="8.5" r="7.5" fill="none" stroke="#34a7d8" stroke-width="1.5"/><path d="M6.5 4.8 L12 8.5 L6.5 12.2Z" fill="#34a7d8"/></svg></div>
    <p class="entry-summary">/ˈkæt/ ? &nbsp;feline mammal usually having thick soft fur and no ability to roar: domestic cats;...</p>
  </div>
  <div class="entry-body">
    <div class="section">
      <h3><b>cat</b> meaning(s)</h3>
      <ul>
        <li>(n) feline mammal usually having thick soft fur and no ability to roar: domestic cats; wildcats</li>
        <li>(n) an informal term for a youth or man</li>
        <li>(n) a spiteful woman gossip</li>
        <li>(n) the leaves of the shrub Catha edulis which are chewed like tobacco or used to make tea; has the effect of a euphoric stimulant</li>
        <li>(n) a whip with nine knotted cords</li>
        <li>(n) a large tracked vehicle that is propelled by two endless metal belts; frequently used for moving earth in construction and farm work</li>
        <li>(n) any of several large cats typically able to roar and living in the wild</li>
        <li>(n) a method of examining body organs by scanning them with X rays and using a computer to construct a series of cross-sectional scans along a single axis</li>
        <li>(v) beat with a cat-o'-nine-tails</li>
        <li>(v) eject the contents of the stomach through the mouth</li>
      </ul>
      <span class="more">more »</span>
    </div>
    <div class="section">
      <h3><b>cat</b> usage(s)</h3>
      <ul>
        <li>NPW: Wildlife reserves alone cannot protect big cats.</li>
        <li>Studies show that the company of a cat can help keep you calm and happy.</li>
      </ul>
      <span class="more">more »</span>
    </div>
    <div class="section">
      <h3>Synonym(s)</h3>
      <p class="synonyms">computed tomography, computerized axial tomography</p>
      <div class="actions"><span class="btn">ADD TO LIST</span><span class="btn">CREATE YOUR OWN</span></div>
    </div>
  </div>
</article>

<article class="entry" style="top:1006px;height:76px">
  <div class="entry-head">
    <div class="entry-word">Cat <svg width="17" height="17" viewBox="0 0 17 17"><circle cx="8.5" cy="8.5" r="7.5" fill="none" stroke="#34a7d8" stroke-width="1.5"/><path d="M6.5 4.8 L12 8.5 L6.5 12.2Z" fill="#34a7d8"/></svg></div>
    <p class="entry-summary">/ˈkæt/ ? &nbsp;feline mammal usually having thick soft fur and no ability to roar: domestic cats;...</p>
  </div>
</article>
<article class="entry" style="top:1085px;height:76px">
  <div class="entry-head">
    <div class="entry-word">Cat <svg width="17" height="17" viewBox="0 0 17 17"><circle cx="8.5" cy="8.5" r="7.5" fill="none" stroke="#34a7d8" stroke-width="1.5"/><path d="M6.5 4.8 L12 8.5 L6.5 12.2Z" fill="#34a7d8"/></svg></div>
    <p class="entry-summary">/ˈkæt/ ? &nbsp;feline mammal usually having thick soft fur and no ability to roar: domestic cats;...</p>
  </div>
</article>
<article class="entry" style="top:1163px;height:37px;border-bottom:0">
  <div class="entry-head">
    <div class="entry-word">Cat <svg width="17" height="17" viewBox="0 0 17 17"><circle cx="8.5" cy="8.5" r="7.5" fill="none" stroke="#34a7d8" stroke-width="1.5"/><path d="M6.5 4.8 L12 8.5 L6.5 12.2Z" fill="#34a7d8"/></svg></div>
  </div>
</article>
</div>
</body>
</html>
```